Veloria....STILL MIND, OPEN HEART

I would like a hologram or golden seed of life as my logo or something along those lines with my business name Veloria and then underneath....STILL MIND, OPEN HEART. Maybe black background....I’m not sure.
On the back, a list of my offerings,
*Harbour of Stillness /Learning to Breathe
*Connection to Source/Self
*Life Changing/Developing
*Plant Medicine consultation
*Conscious Awareness
Veloria_lumen@quillmail.net
Kelwyn: 0427315560
I want my card to look inviting, caring and loving....but with a deep dive into human consciousness 👁💫.
Show me what you got🙏🏽

Designs look the same

```html
<!DOCTYPE html>
<html lang="en">
<head>
<meta charset="utf-8">
<title>Veloria — Business Card</title>
<link href="https://fonts.googleapis.com/css2?family=Montserrat:wght@500;600&display=swap" rel="stylesheet">
<style>
  :root {
    --page-bg: #e4e4e4;
    --page-bg-edge: #d6d6d6;
    --front-glow: #15124f;
    --front-dark: #000004;
    --ink-light: #ffffff;
    --ink-dark: #1d1d44;
    --icon-navy: #0b0b47;
    --ring-warm: #f0506a;
    --ring-violet: #9a3f8e;
    --deco-grey: #b6b6b6;
    --card-white: #ffffff;
  }
  * { margin: 0; padding: 0; box-sizing: border-box; }
  html, body {
    width: 1200px;
    height: 2251px;
    overflow: hidden;
  }
  body {
    position: relative;
    background: radial-gradient(ellipse at 50% 30%, var(--page-bg) 0%, var(--page-bg-edge) 80%);
    font-family: "Montserrat", sans-serif;
  }
  .card {
    position: absolute;
    left: 170px;
    width: 860px;
    height: 520px;
    overflow: hidden;
  }
  .card-front {
    top: 108px;
    background: radial-gradient(ellipse 60% 65% at 50% 35%, var(--front-glow) 0%, #07072a 45%, var(--front-dark) 100%);
    color: var(--ink-light);
    text-align: center;
  }
  .brand-mark {
    position: absolute;
    left: 338px;
    top: 90px;
    width: 184px;
    height: 184px;
    border-radius: 50%;
    border: 8px solid var(--ring-warm);
    border-left-color: var(--ring-violet);
    border-bottom-color: var(--ring-violet);
  }
  .brand-name {
    position: absolute;
    left: 0;
    right: 0;
    top: 318px;
    font-size: 64px;
    font-weight: 600;
    letter-spacing: 1px;
    line-height: 1;
  }
  .tagline {
    position: absolute;
    left: 0;
    right: 0;
    top: 403px;
    font-size: 24px;
    font-weight: 500;
    letter-spacing: 0.5px;
    line-height: 1;
  }
  .card-back {
    top: 689px;
    background: var(--card-white);
    color: var(--ink-dark);
  }
  .deco-ring {
    position: absolute;
    left: 0;
    top: 0;
  }
  .offerings {
    position: absolute;
    left: 58px;
    top: 84px;
    list-style: none;
    font-size: 24px;
    font-weight: 500;
    line-height: 37.6px;
    letter-spacing: 0.4px;
  }
  .offerings li {
    position: relative;
    padding-left: 20px;
  }
  .offerings li::before {
    content: "•";
    position: absolute;
    left: 0;
  }
  .contact {
    position: absolute;
    left: 58px;
    display: flex;
    align-items: center;
    font-size: 23px;
    font-weight: 500;
    letter-spacing: 0.4px;
  }
  .contact-email { top: 357px; }
  .contact-phone { top: 405px; }
  .contact-icon {
    width: 29px;
    height: 25px;
    margin-right: 20px;
    flex-shrink: 0;
  }
</style>
</head>
<body>
  <section class="card card-front" aria-label="Card front">
    <div class="brand-mark" aria-hidden="true"></div>
    <h1 class="brand-name">VELORIA</h1>
    <p class="tagline">STILL MIND, OPEN HEART</p>
  </section>

  <section class="card card-back" aria-label="Card back">
    <svg class="deco-ring" width="860" height="520" viewBox="0 0 860 520" aria-hidden="true">
      <circle cx="706" cy="264" r="238" fill="none" stroke="var(--deco-grey)" stroke-width="13"/>
    </svg>

    <ul class="offerings">
      <li>Harbour of Stillness /<br>Learning to Breathe</li>
      <li>Connection to Source/Self</li>
      <li>Life Changing/Developing</li>
      <li>Plant Medicine consultation</li>
      <li>Conscious Awareness</li>
    </ul>

    <p class="contact contact-email">
      <svg class="contact-icon" viewBox="0 0 29 25" aria-hidden="true">
        <rect width="29" height="25" fill="var(--icon-navy)"/>
        <path d="M4 6 L14.5 14 L25 6" fill="none" stroke="#fff" stroke-width="3" stroke-linejoin="round"/>
      </svg>
      Veloria_lumen@quillmail.net
    </p>
    <p class="contact contact-phone">
      <svg class="contact-icon" viewBox="0 0 29 25" aria-hidden="true">
        <rect width="29" height="25" fill="var(--icon-navy)"/>
        <path d="M8 5 C6 7 6 10 9 14 C12 18 16 21 20 20 L22 17 L18.5 14.5 L16.5 16 C14.5 15 12.5 13 11.5 11 L13 9 L10.5 5.5 Z" fill="#fff"/>
      </svg>
      Kelwyn : 0427315560
    </p>
  </section>
</body>
</html>
```